VORELLI Industrial Maintenance

I offer repair and maintenance services of industrial mechanics in Quebec. I would like a creation that reflects confidence, competence, professionalism and dynamism. I like the orange color and the blue color.

Target Market(s)

Industries and Manufacturing companies using industrial machinery for the manufacture of their products.

Industry/Entity Type

Manufacturing

Contact Information for Business Card

VORELLI Maintenance Industrielle
Tél: (450)-318-5907
Courriel: vorelli.mnt@brastomail.com

Font styles to use
Sans Serif

Colors
f78f20
0455a3

Requirements
Must have
• My company name: VORELLI Maintenance Industrielle My phone: (450) -318-5907 My email: vorelli.mnt@brastomail.com
Nice to have
• Integrate a representative logo of the mechanics (gears, mechanical parts)

```html
<!DOCTYPE html>
<html lang="en">
<head>
<meta charset="utf-8">
<title>VORELLI Maintenance Industrielle — Business Card</title>
<link rel="stylesheet" href="https://fonts.googleapis.com/css2?family=Open+Sans:wght@400;600;700&display=swap">
<style>
  :root {
    --page-bg: #e9e7e4;
    --card-bg: #ffffff;
    --ink-dark: #333333;
    --ink-muted: #6b6b6b;
    --brand-blue: #2a61a3;
    --band-dark: #2a2a2a;
    --band-gray: #a3a3a3;
    --rule: #bdbdbd;
  }
  * { box-sizing: border-box; margin: 0; padding: 0; }
  html, body {
    width: 1200px;
    height: 1000px;
    overflow: hidden;
    background: var(--page-bg);
    font-family: "Open Sans", Arial, sans-serif;
  }
  .business-card {
    position: absolute;
    left: 266px;
    width: 666px;
    height: 397px;
    background: var(--card-bg);
    box-shadow: 0 6px 14px rgba(0,0,0,0.25);
    overflow: hidden;
  }
  .business-card--top { top: 74px; }
  .business-card--bottom { top: 533px; }

  .brand-name {
    position: absolute;
    left: 33px;
    top: 78px;
    width: 256px;
    text-align: center;
    color: var(--brand-blue);
    font-weight: 700;
    line-height: 1.15;
  }
  .brand-name__main { display: block; font-size: 44px; letter-spacing: 1px; }
  .brand-name__sub { display: block; font-size: 13.5px; letter-spacing: 0.6px; text-transform: uppercase; }

  .contact-person {
    position: absolute;
    left: 33px;
    top: 229px;
  }
  .contact-person__name {
    font-size: 22px;
    font-weight: 600;
    color: var(--ink-dark);
    line-height: 1.2;
  }
  .contact-person__role {
    font-size: 16.5px;
    color: var(--ink-muted);
    line-height: 1.3;
  }
  .contact-rule {
    position: absolute;
    left: 33px;
    top: 284px;
    width: 366px;
    height: 1.5px;
    background: var(--rule);
  }
  .contact-list {
    position: absolute;
    left: 33px;
    top: 296px;
    list-style: none;
    font-size: 16.5px;
    color: var(--ink-muted);
    line-height: 24px;
  }
  .contact-list li { display: flex; align-items: center; gap: 6px; }
  .contact-list svg { width: 15px; height: 13px; fill: var(--brand-blue); }

  .card-bands {
    position: absolute;
    left: 0;
    bottom: 0;
    width: 666px;
    height: 397px;
  }
  .band-dark { fill: var(--band-dark); }
  .band-gray { fill: var(--band-gray); }
  .band-blue { fill: var(--brand-blue); }
</style>
</head>
<body>

<section class="business-card business-card--top">
  <div class="brand-name">
    <span class="brand-name__main">VORELLI</span>
    <span class="brand-name__sub">Maintenance Industrielle</span>
  </div>
  <div class="contact-person">
    <p class="contact-person__name">Daniel Marchetti</p>
    <p class="contact-person__role">CEO / Owner</p>
  </div>
  <div class="contact-rule"></div>
  <ul class="contact-list">
    <li><svg viewBox="0 0 16 14" aria-hidden="true"><path d="M1 5 Q8 -1 15 5 L12 6 L11 4 Q8 3 5 4 L4 6 Z M3 8 L13 8 L14 13 L2 13 Z"/></svg>(450) -318-5907</li>
    <li><svg viewBox="0 0 16 14" aria-hidden="true"><path d="M1 2 H15 V12 H1 Z M2 3 L8 8 L14 3 Z" fill-rule="evenodd"/></svg>vorelli.mnt@brastomail.com</li>
  </ul>
  <svg class="card-bands" viewBox="0 0 666 397" aria-hidden="true">
    <polygon class="band-dark" points="0,361 349,361 326,397 0,397"/>
    <polygon class="band-gray" points="355,362 666,362 666,371 349,371"/>
    <polygon class="band-blue" points="345,378 666,378 666,397 333,397"/>
  </svg>
</section>

<section class="business-card business-card--bottom">
  <div class="brand-name">
    <span class="brand-name__main">VORELLI</span>
    <span class="brand-name__sub">Maintenance Industrielle</span>
  </div>
  <div class="contact-person">
    <p class="contact-person__name">Daniel Marchetti</p>
    <p class="contact-person__role">CEO / Owner</p>
  </div>
  <div class="contact-rule"></div>
  <ul class="contact-list">
    <li><svg viewBox="0 0 16 14" aria-hidden="true"><path d="M1 5 Q8 -1 15 5 L12 6 L11 4 Q8 3 5 4 L4 6 Z M3 8 L13 8 L14 13 L2 13 Z"/></svg>(450) -318-5907</li>
    <li><svg viewBox="0 0 16 14" aria-hidden="true"><path d="M1 2 H15 V12 H1 Z M2 3 L8 8 L14 3 Z" fill-rule="evenodd"/></svg>vorelli.mnt@brastomail.com</li>
  </ul>
  <svg class="card-bands" viewBox="0 0 666 397" aria-hidden="true">
    <polygon class="band-dark" points="0,361 349,361 326,397 0,397"/>
    <polygon class="band-gray" points="355,362 666,362 666,371 349,371"/>
    <polygon class="band-blue" points="345,378 666,378 666,397 333,397"/>
  </svg>
</section>

</body>
</html>
```